Larkspur Ridge Management - Business Cards

I need business cards. My current logo was designed by a designer at this site and I very much like and am happy with the results. I would like a business card that is trendy, unique, current yet professional. I deal with high net worth clients daily

Target Market(s)

Out of state investors looking to get into the rental market in Ohio

Industry/Entity Type

Property Management, Consulting

Contact Information for Business Card

Name, Title (Chief Financial Officer) office phone number (555) 817-3094 website address larkridgemgmt.example

Font styles to use
Sans Serif

Colors
0054AA
0677BA
7BADD7
CADEEF
E8F1F8
0094D4
00A9DD
6FCCEA
C7EBF8
E9F6FB
00AB8E
00BBA5
67D7C9
C6EFE9
E9F9F6

```html
<!DOCTYPE html>
<html lang="en">
<head>
<meta charset="utf-8">
<title>Larkspur Ridge Management – Business Cards</title>
<link rel="stylesheet" href="https://fonts.googleapis.com/css2?family=Montserrat:wght@400;500;700;800&display=swap">
<style>
  :root {
    --backdrop: #f1efea;
    --blue-deep: #0054aa;
    --blue-mid: #0677ba;
    --blue-soft: #7badd7;
    --blue-pale: #c7ebf8;
    --sky: #6fccea;
    --teal: #00bba5;
    --teal-light: #67d7c9;
    --white: #ffffff;
    --card-shadow: 0 10px 24px rgba(0, 40, 80, 0.28);
  }
  * { box-sizing: border-box; margin: 0; padding: 0; }
  html, body {
    width: 1140px;
    height: 1200px;
    overflow: hidden;
    background: var(--backdrop);
    font-family: "Montserrat", Arial, sans-serif;
  }
  .sheet { position: relative; width: 1140px; height: 1200px; }

  .card {
    position: absolute;
    left: 181px;
    width: 778px;
    box-shadow: var(--card-shadow);
    overflow: hidden;
  }

  /* Front */
  .card--front {
    top: 162px;
    height: 422px;
    background: var(--blue-deep);
  }
  .card__frame { position: absolute; inset: 0; width: 100%; height: 100%; }
  .front__name {
    position: absolute;
    left: 0; right: 0;
    top: 150px;
    text-align: center;
    color: var(--white);
    font-weight: 800;
    font-size: 42px;
    line-height: 1.15;
    letter-spacing: 0.5px;
    text-transform: uppercase;
  }

  /* Back */
  .card--back {
    top: 629px;
    height: 440px;
    background: var(--blue-mid);
  }
  .back__name {
    position: absolute;
    left: 50px;
    top: 150px;
    width: 300px;
    text-align: center;
    color: var(--white);
    font-weight: 800;
    font-size: 30px;
    line-height: 1.15;
    text-transform: uppercase;
  }
  .holder {
    position: absolute;
    left: 406px;
    top: 130px;
    right: 0;
  }
  .holder__name {
    font-size: 27px;
    font-weight: 500;
    letter-spacing: 0.6px;
    color: var(--blue-pale);
    text-transform: uppercase;
    white-space: nowrap;
  }
  .holder__name strong { font-weight: 700; color: var(--teal-light); }
  .holder__title {
    margin-top: 10px;
    font-size: 20px;
    font-weight: 500;
    color: var(--white);
    text-transform: uppercase;
    white-space: nowrap;
  }
  .holder__rule {
    margin-top: 28px;
    height: 2px;
    background: var(--blue-soft);
  }
  .contact { list-style: none; margin-top: 28px; }
  .contact__item {
    display: flex;
    align-items: center;
    gap: 12px;
    font-size: 19px;
    color: var(--white);
    height: 30px;
    margin-bottom: 8px;
    white-space: nowrap;
  }
  .contact__icon { width: 24px; height: 24px; flex: none; }
</style>
</head>
<body>
<main class="sheet">

  <section class="card card--front" aria-label="Business card front">
    <svg class="card__frame" viewBox="0 0 778 422" aria-hidden="true">
      <path d="M209 404 H18 V18 H760 V404 H569" fill="none" stroke="var(--teal)" stroke-width="3"/>
      <line x1="224" y1="404" x2="554" y2="404" stroke="var(--sky)" stroke-width="3"/>
    </svg>
    <p class="front__name">Larkspur Ridge<br>Management</p>
  </section>

  <section class="card card--back" aria-label="Business card back">
    <p class="back__name">Larkspur Ridge<br>Management</p>

    <div class="holder">
      <h1 class="holder__name">Marin T. <strong>Ellsworth</strong></h1>
      <p class="holder__title">Chief Financial Officer</p>
      <div class="holder__rule"></div>
      <ul class="contact">
        <li class="contact__item">
          <svg class="contact__icon" viewBox="0 0 24 24" aria-hidden="true">
            <path fill="var(--white)" d="M6.6 10.8a15.2 15.2 0 0 0 6.6 6.6l2.2-2.2a1 1 0 0 1 1-.25 11.4 11.4 0 0 0 3.6.57 1 1 0 0 1 1 1V20a1 1 0 0 1-1 1A17 17 0 0 1 3 4a1 1 0 0 1 1-1h3.5a1 1 0 0 1 1 1c0 1.25.2 2.45.57 3.57a1 1 0 0 1-.25 1z"/>
          </svg>
          <span>Phone: (555) 817-3094</span>
        </li>
        <li class="contact__item">
          <svg class="contact__icon" viewBox="0 0 24 24" aria-hidden="true" fill="none" stroke="var(--white)" stroke-width="1.7">
            <circle cx="12" cy="12" r="9.5"/>
            <ellipse cx="12" cy="12" rx="4.2" ry="9.5"/>
            <line x1="2.5" y1="12" x2="21.5" y2="12"/>
            <path d="M4.2 7h15.6M4.2 17h15.6"/>
          </svg>
          <span>Website: larkridgemgmt.example</span>
        </li>
      </ul>
    </div>
  </section>

</main>
</body>
</html>
```